Book cover for book about ex-wifes

I need a book cover for my new book called "Tidligere brude fra Solen, Stormen og Lindevang" - In english: "Former brides from Sun, Storm and Lindevang" (Hørsholm is a posh city in Denmark).

The book is by men for men about ex-wifes and about how to avoid getting them.
Is it a book from a sexologist and couples therapist to men on how to improve relations.

Men (and curious women)

• Something that indicate three types of ex-wifes

And the author name “Jonas Beltoft”
• Something that says something about relationships, couples and how to stay together (or how to avoid not breaking up)
• No hate

```html
<!DOCTYPE html>
<html lang="da">
<head>
<meta charset="utf-8">
<title>Tidligere brude fra Solen, Stormen og Lindevang – omslag</title>
<link rel="stylesheet" href="https://fonts.googleapis.com/css2?family=Fjalla+One&family=Josefin+Sans:wght@600&family=Fira+Sans+Condensed:wght@400&display=swap">
<style>
  :root {
    --page: #f1f1f1;
    --slate: #2b2f36;
    --slate-deep: #23272d;
    --paper-grey: #8f9091;
    --paper-edge: #e7e0cf;
    --ink: #111214;
    --title-light: #eceae6;
    --title-muted: #8a8c8f;
    --figure: #a9abad;
    --body-text: #e4e4e4;
  }
  * { margin: 0; padding: 0; box-sizing: border-box; }
  html, body { width: 899px; height: 1200px; overflow: hidden; background: var(--page); }
  .canvas { position: relative; width: 899px; height: 1200px; }

  .cover-spread {
    position: absolute; left: 20px; top: 301px;
    width: 860px; height: 597px;
    background: radial-gradient(ellipse at 40% 40%, var(--slate), var(--slate-deep));
    box-shadow: 0 2px 8px rgba(0,0,0,.18);
    overflow: hidden;
  }

  /* Back cover */
  .back-cover { position: absolute; left: 0; top: 0; width: 401px; height: 597px; }
  .back-title {
    position: absolute; left: 64px; top: 80px;
    font-family: "Fjalla One", sans-serif; font-size: 20px; line-height: 22px;
    text-transform: uppercase; color: var(--title-light);
  }
  .back-title .muted { color: var(--title-muted); display: block; }
  .blurb {
    position: absolute; left: 64px; top: 146px; width: 264px;
    font-family: "Fira Sans Condensed", sans-serif; font-size: 9.6px; line-height: 12.9px;
    color: var(--body-text); text-align: justify; hyphens: auto;
  }
  .blurb p + p { margin-top: 13px; }

  /* Spine */
  .spine { position: absolute; left: 401px; top: 0; width: 63px; height: 597px; }
  .spine-title {
    position: absolute; left: 50px; top: 58px;
    transform: rotate(90deg); transform-origin: left top;
    white-space: nowrap;
    font-family: "Fjalla One", sans-serif; font-size: 18px; line-height: 19px;
    text-transform: uppercase; color: var(--title-light);
  }
  .spine-title .muted { color: var(--title-muted); display: block; }
  .spine-author {
    position: absolute; left: 40px; top: 340px;
    transform: rotate(90deg); transform-origin: left top; white-space: nowrap;
    font-family: "Josefin Sans", sans-serif; font-weight: 600; font-size: 11px;
    letter-spacing: 12px; color: var(--title-muted);
  }

  /* Front cover */
  .front-cover { position: absolute; left: 464px; top: 0; width: 396px; height: 597px; }
  .front-top {
    position: absolute; left: 0; top: 0; width: 396px; height: 252px;
    background: radial-gradient(ellipse at 30% 40%, #9a9b9c, var(--paper-grey));
  }
  .torn-edge { position: absolute; left: 0; top: 244px; width: 396px; height: 16px; }
  .front-author {
    position: absolute; right: 26px; top: 52px;
    font-family: "Josefin Sans", sans-serif; font-weight: 600; font-size: 16px;
    letter-spacing: 14px; margin-right: -14px; color: var(--ink);
  }
  .front-title {
    position: absolute; right: 26px; top: 108px; text-align: right;
    font-family: "Fjalla One", sans-serif; font-size: 24px; line-height: 26px;
    text-transform: uppercase; color: var(--title-light);
  }
  .front-title .dark { color: var(--ink); display: block; }
  .couple-illustration {
    position: absolute; left: 32px; top: 278px; width: 300px; height: 319px;
    background: radial-gradient(ellipse at 50% 75%, var(--figure), rgba(169,171,173,.25) 70%, transparent 100%);
  }
</style>
</head>
<body>
<div class="canvas">
  <section class="cover-spread">
    <div class="back-cover">
      <h2 class="back-title">Tidligere brude fra Solen,<span class="muted">Stormen og Lindevang</span></h2>
      <div class="blurb">
        <p>Lorem ipsum dolor sit amet, consectetur adipiscing elit. Nam viverra lorem nec nibh porttitor dapibus. Donec fringilla pretium lorem, quis ultrices leo eleifend interdum. Aliquam ante diam, blandit sed scelerisque posuere, vestibulum et elit. Sed feugiat mauris orci, nec semper libero tristique at. Etiam ut est in velit facilisis placerat eget sed est. Fusce at enim nec libero vulputate cursus. Phasellus sodales eu lectus et fermentum. Aenean erat enim, pharetra eu interdum vel, elementum sit amet ex. Etiam sit amet efficitur augue, vitae malesuada nulla. Fusce a ultrices nulla. Quisque viverra luctus leo, vitae aliquam massa vehicula facilisis. Aenean iaculis imperdiet risus a dignissim. Nulla rhoncus sem ex, non molestie nulla laoreet ac. Class aptent taciti sociosqu ad litora torquent per conubia nostra, per inceptos himenaeos. Sed sagittis magna accumsan sagittis porta. Donec pretium erat at convallis dapibus.</p>
        <p>Quisque metus magna, hendrerit non eros venenatis, hendrerit feugiat diam. Fusce aliquam odio euismod, finibus ex vitae, viverra mauris. Suspendisse auctor urna eu augue bibendum consectetur. Sed eu orci vitae dolor luctus ornare. Morbi nisl risus, euismod ac pretium id, ultricies vitae libero. Sed placerat ac eros nec auctor. Nunc dignissim magna nisi, ac dictum ipsum consectetur non. Phasellus nec blandit ipsum. Donec eget nisl lacinia, aliquet justo eget, molestie felis. Pellentesque ultrices ante nec molestie consectetur. Integer in ipsum nec ipsum sollicitudin viverra.</p>
      </div>
    </div>

    <div class="spine">
      <div class="spine-title">Tidligere brude fra Solen,<span class="muted">Stormen og Lindevang</span></div>
      <div class="spine-author">AUTHOR NAME</div>
    </div>

    <div class="front-cover">
      <div class="front-top"></div>
      <svg class="torn-edge" viewBox="0 0 396 16" preserveAspectRatio="none" aria-hidden="true">
        <polyline fill="none" stroke="var(--paper-edge)" stroke-width="3"
          points="0,8 12,6 22,9 35,5 48,9 60,6 74,10 86,6 99,8 112,5 126,9 139,6 152,9 166,5 180,8 193,6 206,10 220,6 233,8 247,5 260,9 274,6 288,9 301,5 315,8 328,6 342,10 356,6 369,8 383,5 396,8"/>
      </svg>
      <div class="front-author">AUTHOR NAME</div>
      <h1 class="front-title">Tidligere brude fra Solen,<span class="dark">Stormen og Lindevang</span></h1>
      <div class="couple-illustration" role="img" aria-label="Grey silhouettes of a woman and a man arguing face to face, with question marks above their heads"></div>
    </div>
  </section>
</div>
</body>
</html>
```